Tuition Center Website

We need a new web site for a tutoring company based in sydney.

We only teach senior highschool students and pride ourselves on building the students abilities to think their way through life.

I would like a bright and vibrant website that looks professional and modern.
It needs to look simple and neat but also have the functionality we need.
Images and flash would be good.

Please keep in mind that the site must be appealing to a younger audience.

We need a multipage website with the following navigation bars:

1.Home (As logo not "home" button)
I would like a news box/ticker somewhere that can stream our chatterbook and peeplr feeds and also any news updates we want to put up.
Subscribe to newsletter button.

2. About us.
This needs to be a pull down into:
-What we do
-Why we do it
-How we do it

3. Courses
Pulldown into:
-Maths
-English
-Science
(we may need to attach extra pages behind these e.g. Courses/Science/Physics or Courses/Science/Chemistry and possibly add a link to a new formvik form)

4. Inspired
This page is like a blog page where we can upload videos, links to articles that we find to be inspiring and hopefully will inspire others.

5. Inspire
This is a recruitment page. Only content here.

6. Contact us.
Trovix map widget and a 'contact us' form

* Our branding requires green close to #12FF3D

***Please have a look at the current website.
@ www.velmoralearning.com.au

Thanks everybody hope the revision of my brief is better and more informative than my last one
Updates

Target Market(s)

senior highschool students aged 15-19, parents ( to a lesser degree)

Industry/Entity Type

It Company

Requirements
Must have
• Ability to change content on pages.

The green doesn't have to be everywhere, but it must be obvious that it is our colour.

Nice to have
• Sites with a nicer mix of images and flash will be given more consideration. But then again, if you amaze us, you amaze us and we will go with your design.
Should not have
• Should stay away from ocre, brown colours and serif fonts.

```html
<!DOCTYPE html>
<html lang="en">
<head>
<meta charset="utf-8">
<title>Registration – Velmora Learning</title>
<link rel="stylesheet" href="https://fonts.googleapis.com/css2?family=Signika:wght@400;600&family=Open+Sans:wght@400;600&display=swap">
<style>
  :root {
    --slate-top: #55626f;
    --slate-bottom: #3f4c59;
    --slate-line: #2f3a45;
    --btn-dark: #3a4652;
    --btn-dark-line: #2e3842;
    --logo-green: #5ee000;
    --coral: #f27b68;
    --coral-dark: #d9604e;
    --ink: #3d3d3d;
    --muted: #9a9a9a;
    --field-line: #cfcfcf;
    --white: #ffffff;
    --divider: #d4d4d4;
    --owner-text: #6c7884;
  }
  * { box-sizing: border-box; margin: 0; padding: 0; }
  html, body { width: 1200px; height: 596px; overflow: hidden; background: var(--white); }
  body { position: relative; font-family: "Open Sans", Arial, sans-serif; color: var(--ink); }

  .site-header {
    position: absolute; left: 0; top: 0; width: 1200px; height: 85px;
    background: linear-gradient(var(--slate-top), var(--slate-bottom));
    border-bottom: 1px solid var(--slate-line);
  }
  .brand {
    position: absolute; left: 101px; top: 13px; width: 164px; height: 59px;
    background: var(--white);
    display: flex; align-items: center; justify-content: center; gap: 7px;
  }
  .brand-mark { width: 12px; height: 12px; background: var(--logo-green); }
  .brand-name { font-weight: 600; font-size: 16px; color: var(--logo-green); }

  .main-nav {
    position: absolute; right: 342px; top: 32px;
    display: flex; gap: 19px;
  }
  .main-nav a {
    font-family: "Signika", Arial, sans-serif; font-weight: 600;
    font-size: 13.5px; line-height: 18px; color: var(--white); text-decoration: none; white-space: nowrap;
  }
  .icon-btn {
    position: absolute; top: 29px; width: 28px; height: 26px; border-radius: 3px;
    background: var(--btn-dark); border: 1px solid var(--btn-dark-line);
    display: flex; align-items: center; justify-content: center;
  }
  .pill-btn {
    position: absolute; top: 29px; height: 26px; border-radius: 3px;
    display: flex; align-items: center; gap: 6px; padding-left: 10px;
    font-size: 12px; color: var(--white); white-space: nowrap;
  }
  .pill-btn.dark { left: 944px; width: 68px; background: var(--btn-dark); border: 1px solid var(--btn-dark-line); }
  .pill-btn.accent { left: 1022px; width: 78px; background: var(--coral); border: 1px solid var(--coral-dark); }

  .page-banner {
    position: absolute; left: 0; top: 86px; width: 1200px; height: 71px;
    background: linear-gradient(90deg, #a3a8ab 0%, #8fa0a8 10%, #5f95b8 24%, #9aa9b2 34%, #7fae6a 44%, #b9bfc2 54%, #6d8fa8 64%, #55636b 74%, #8fb19a 84%, #a7adb1 100%);
  }
  .page-title {
    position: absolute; left: 99px; top: 106px; font-family: "Signika", Arial, sans-serif;
    font-weight: 400; font-size: 23px; line-height: 30px; color: var(--white);
  }

  .form-heading {
    position: absolute; top: 204px; font-family: "Signika", Arial, sans-serif;
    font-size: 17px; line-height: 22px; font-weight: 400; color: var(--ink);
  }
  .field {
    position: absolute; height: 29px; border: 1px solid var(--field-line); border-radius: 3px;
    background: var(--white); box-shadow: inset 0 1px 2px rgba(0,0,0,.08);
    padding-left: 9px; display: flex; align-items: center; font-size: 11.5px; color: var(--muted);
  }
  .field.filled { color: var(--ink); }
  .action-btn {
    position: absolute; top: 330px; height: 28px; border-radius: 3px;
    background: var(--coral); border: 1px solid var(--coral-dark);
    display: flex; align-items: center; gap: 7px; padding-left: 10px;
    font-size: 12px; color: var(--white); white-space: nowrap;
  }
  .column-divider {
    position: absolute; left: 754px; top: 244px; height: 86px;
    border-left: 1px dotted var(--divider);
  }

  .site-footer {
    position: absolute; left: 0; top: 543px; width: 1200px; height: 53px;
    background: linear-gradient(var(--slate-top), var(--slate-bottom));
    border-top: 1px solid var(--slate-line);
  }
  .copyright { position: absolute; left: 94px; top: 20px; font-size: 11.5px; color: var(--white); }
  .copyright .owner { color: var(--owner-text); }
  .footer-nav {
    position: absolute; right: 99px; top: 21px; display: flex; gap: 13px;
  }
  .footer-nav a { font-size: 11.5px; color: var(--white); text-decoration: none; white-space: nowrap; }
</style>
</head>
<body>
  <header class="site-header">
    <div class="brand"><span class="brand-mark"></span><span class="brand-name">velmora learning</span></div>
    <nav class="main-nav">
      <a>Home</a>
      <a>Courses</a>
      <a>About</a>
      <a>Inspired</a>
      <a>Inspire</a>
      <a>Contact</a>
    </nav>
    <div class="icon-btn" style="left:870px">
      <svg width="11" height="11" viewBox="0 0 11 11"><path d="M5.5 0v11M0 5.5h11" stroke="#fff" stroke-width="2"/></svg>
    </div>
    <div class="icon-btn" style="left:907px">
      <svg width="11" height="11" viewBox="0 0 11 11"><circle cx="4.5" cy="4.5" r="3.3" fill="none" stroke="#fff" stroke-width="1.6"/><path d="M7 7l3.3 3.3" stroke="#fff" stroke-width="1.8"/></svg>
    </div>
    <div class="pill-btn dark">
      <svg width="7" height="13" viewBox="0 0 7 13"><circle cx="3.5" cy="3.5" r="3" fill="#fff"/><rect x="2.5" y="5" width="2" height="8" fill="#fff"/></svg>Sign In
    </div>
    <div class="pill-btn accent">
      <svg width="12" height="11" viewBox="0 0 12 11"><circle cx="6" cy="3" r="3" fill="#fff"/><path d="M0 11c0-4 3-5 6-5s6 1 6 5z" fill="#fff"/></svg>Register
    </div>
  </header>

  <div class="page-banner" role="img" aria-label="Blurred photograph of a row of book spines on a shelf"></div>
  <h1 class="page-title">Registration</h1>

  <main>
    <h2 class="form-heading" style="left:99px">Register</h2>
    <div class="field" style="left:99px;top:245px;width:297px">Username</div>
    <div class="field" style="left:419px;top:245px;width:297px">Email</div>
    <div class="field" style="left:99px;top:287px;width:297px">Password</div>
    <div class="field" style="left:419px;top:287px;width:297px">Repeat Password</div>
    <div class="action-btn" style="left:99px;width:80px">
      <svg width="12" height="11" viewBox="0 0 12 11"><circle cx="6" cy="3" r="3" fill="#fff"/><path d="M0 11c0-4 3-5 6-5s6 1 6 5z" fill="#fff"/></svg>Register
    </div>

    <div class="column-divider"></div>

    <h2 class="form-heading" style="left:793px">Sign In</h2>
    <div class="field filled" style="left:793px;top:245px;width:307px">Demo</div>
    <div class="field filled" style="left:793px;top:287px;width:307px;letter-spacing:1px">••••</div>
    <div class="action-btn" style="left:793px;width:69px">
      <svg width="7" height="13" viewBox="0 0 7 13"><circle cx="3.5" cy="3.5" r="3" fill="#fff"/><rect x="2.5" y="5" width="2" height="8" fill="#fff"/></svg>Sign In
    </div>
  </main>

  <footer class="site-footer">
    <p class="copyright"><span class="owner">Velmora Learning</span> © 2013</p>
    <nav class="footer-nav">
      <a>Home</a>
      <a>Courses</a>
      <a>About</a>
      <a>Inspired</a>
      <a>Inspire</a>
      <a>Contact</a>
    </nav>
  </footer>
</body>
</html>
```